Creation of a book cover
Size : 14 x 20,5 cm (+ 5 mm bleed area at the top, bottom and right areas)
The Title is a French sentence which means “The heron dreaming on the cold roof of this empty station”. It’s a surrealistic title which has no link to the story.
AUTHOR : Mathieu Vorlange
TITLE : "Le héron rêvant sur le toit froid de cette gare vide »
PUBLISHER (AT THE BOTTOM OF THE PAGE) : Editions Parvenche
I send a PDF file with the kind of cover we have imagine, but you can propose something different. The glass and the fly can of course be used.

```html
<!DOCTYPE html>
<html lang="fr">
<head>
<meta charset="utf-8">
<title>Le héron rêvant sur le toit froid de cette gare vide — couverture</title>
<link rel="stylesheet" href="https://fonts.googleapis.com/css2?family=Open+Sans:ital,wght@0,400;0,700;1,300&family=Jost:wght@300;400&family=Libre+Baskerville:wght@700&family=Arimo&display=swap">
<style>
  :root {
    --page-bg: #ffffff;
    --ink-light: #f2f2ef;
    --ink-soft: #e4e6e2;
    --cover-dark: #141a17;
    --cover-mid: #2b3531;
    --cover-fog: #56625c;
    --spine: #1f2b27;
    --spine-edge: #0f1513;
    --slot: #e6e6e6;
    --slot-text: #8a8a8a;
  }
  * { margin: 0; padding: 0; box-sizing: border-box; }
  html, body { width: 1200px; height: 960px; overflow: hidden; background: var(--page-bg); }
  .jacket {
    position: absolute; left: 20px; top: 70px;
    width: 1160px; height: 821px;
    display: flex;
  }
  .panel { position: relative; height: 100%; overflow: hidden; color: var(--ink-light); }
  .back-cover, .front-cover { width: 537px; }
  .artwork { position: absolute; inset: 0; }
  .back-cover .artwork {
    background:
      radial-gradient(ellipse 60% 30% at 55% 12%, rgba(120,130,125,.45), transparent 70%),
      radial-gradient(ellipse 80% 25% at 50% 68%, rgba(70,82,76,.35), transparent 70%),
      linear-gradient(180deg, #1a211e 0%, #26302c 40%, #1c2421 70%, var(--cover-dark) 100%);
  }
  .front-cover .artwork {
    background:
      radial-gradient(ellipse 55% 30% at 55% 18%, rgba(150,160,155,.45), transparent 70%),
      radial-gradient(ellipse 35% 30% at 58% 62%, rgba(160,170,165,.28), transparent 70%),
      linear-gradient(180deg, #2a3430 0%, var(--cover-fog) 25%, #3a4641 50%, #2a2a24 78%, #17150f 100%);
  }
  .spine {
    width: 86px;
    background: var(--spine);
    border-left: 2px solid var(--spine-edge);
    border-right: 2px solid var(--spine-edge);
  }
  .spine-text {
    position: absolute; left: 50%; top: 20px;
    transform-origin: left top;
    transform: rotate(90deg) translateY(-50%);
    white-space: nowrap;
    display: flex; align-items: center; gap: 12px;
  }
  .spine-title { font: 400 30px/1 "Open Sans", sans-serif; letter-spacing: .5px; }
  .spine-bar { width: 3px; height: 30px; background: var(--ink-light); }
  .spine-publisher { font: 300 24px/1 "Jost", sans-serif; letter-spacing: 8px; }

  /* back cover */
  .back-heading {
    position: absolute; left: 53px; top: 68px;
    font: 700 19px/1 "Open Sans", sans-serif; letter-spacing: 4px;
  }
  .back-subheading {
    position: absolute; left: 53px; top: 92px;
    font: italic 300 18px/1.2 "Open Sans", sans-serif;
  }
  .author-photo-slot {
    position: absolute; left: 45px; top: 130px;
    width: 112px; height: 144px; background: var(--slot);
  }
  .blurb {
    position: absolute; font: 400 12.3px/1.32 "Arimo", sans-serif;
    text-align: justify; hyphens: auto; color: var(--ink-soft);
  }
  .blurb p + p { margin-top: 15px; }
  .blurb-intro { left: 179px; top: 160px; width: 313px; }
  .blurb-main { left: 34px; top: 287px; width: 460px; }
  .blurb-main .plain { text-align: left; }
  .isbn-slot {
    position: absolute; left: 30px; top: 712px;
    width: 176px; height: 90px; background: var(--slot);
    display: flex; align-items: center; justify-content: center;
    font: 300 26px/1 "Jost", sans-serif; letter-spacing: 8px; color: var(--slot-text);
  }
  .back-credits { position: absolute; left: 222px; top: 752px; }
  .back-publisher { font: 300 16px/1 "Jost", sans-serif; letter-spacing: 3.5px; }
  .back-author { margin-top: 10px; font: 400 17px/1 "Jost", sans-serif; letter-spacing: 3.5px; }

  /* front cover */
  .front-author {
    position: absolute; left: 0; right: 0; top: 50px; text-align: center;
    font: 400 24px/1 "Jost", sans-serif; letter-spacing: 5px;
  }
  .front-title {
    position: absolute; left: 0; right: 0; top: 125px; text-align: center;
    font: 700 60px/1 "Libre Baskerville", serif; letter-spacing: 1px;
  }
  .front-subtitle {
    position: absolute; left: 40px; right: 40px; top: 208px; text-align: center;
    font: italic 300 25px/1.35 "Open Sans", sans-serif; color: var(--ink-soft);
  }
  .front-publisher {
    position: absolute; left: 0; right: 0; top: 760px; text-align: center;
    font: 300 26px/1 "Jost", sans-serif; letter-spacing: 6px;
  }
</style>
</head>
<body>
<main class="jacket">

  <section class="panel back-cover">
    <div class="artwork" role="img" aria-label="Paysage brumeux et sombre : ciel nuageux, maisons et cimetière dans le brouillard"></div>
    <h2 class="back-heading">TEXTE DE QUATRIÈME</h2>
    <p class="back-subheading">de couverture (en français)</p>
    <div class="author-photo-slot"></div>
    <div class="blurb blurb-intro">
      <p>Dans ce récit délicat et profondément original, Mathieu Vorlange nous invite à porter un regard neuf sur l’insignifiant, à travers la contemplation d’un simple verre d’eau et d’une mouche qui s’y pose. Mais ce qui semble au premier abord anodin devient, sous sa plume, une porte ouverte vers une réflexion plus vaste sur la vie, le temps, et notre place dans le monde.</p>
    </div>
    <div class="blurb blurb-main">
      <p>Avec une élégance ironique et un sens aigu de l’observation, l’auteur tisse une fable contemporaine où chaque détail révèle un sens caché. Les gestes les plus quotidiens prennent une résonance inattendue, les silences deviennent parole, et l’absurde se fait révélateur de vérités profondes.</p>
      <p>Ce livre raconte l’histoire d’un homme ordinaire, témoin silencieux d’une scène simple mais chargée de mystère. Tandis qu’il observe la mouche et son rituel inattendu, il se surprend à devenir lui-même l’objet d’un regard. Entre humour subtil, tendresse pour la condition humaine et clins d’œil littéraires, Mathieu Vorlange déploie un univers où le réel et l’imaginaire se confondent.</p>
      <p>« Observer, c’est déjà changer le monde. »<br>Ce roman est une invitation à ralentir, à s’émerveiller, et à retrouver cette capacité à voir l’invisible dans l’ordinaire.</p>
      <p class="plain">Alors, êtes-vous prêts à voir la mouche autrement ?<br>Et surtout, à découvrir ce qu’elle peut vous apprendre sur vous-même ?</p>
    </div>
    <div class="isbn-slot">ISBN</div>
    <div class="back-credits">
      <p class="back-publisher">ÉDITIONS PARVENCHE</p>
      <p class="back-author">MATHIEU VORLANGE</p>
    </div>
  </section>

  <section class="panel spine">
    <div class="spine-text">
      <span class="spine-title">LE HÉRON</span>
      <span class="spine-bar"></span>
      <span class="spine-publisher">ÉDITIONS PARVENCHE</span>
    </div>
  </section>

  <section class="panel front-cover">
    <div class="artwork" role="img" aria-label="Illustration : une mouche posée sur le bord d’un verre d’eau, sur une table en bois, devant un paysage brumeux"></div>
    <p class="front-author">MATHIEU VORLANGE</p>
    <h1 class="front-title">LE HÉRON</h1>
    <p class="front-subtitle">RÊVANT SUR LE TOIT FROID DE CETTE GARE VIDE</p>
    <p class="front-publisher">ÉDITIONS PARVENCHE</p>
  </section>

</main>
</body>
</html>
```